Fresh Rally Quest

I need a design for and advertisement on a Screen at a Doctor's Surgery. The ad would be up for 15 seconds then on a rotation which last 10 minutes. So every 10 minutes if you are sitting in the Doctor's waiting room you will see my ad for 15 seconds.

I am a Personal Trainer and my company is TrueForm Habits. I need this advertisement for my January promotion, I will be running the ad in December. So I need the ad to send to the agent by this Friday.

I attach something for you to start with, basically person sitting in the doctor's waiting room must see headline, value of offer discounted price and webpage. The rest of the stuff should be on ad for those sitting in the waiting room for a long time.

This is a really important ad as January is the biggest month for Personal Trainers, I can't mess this up

Reason: So I've decided it makes sense to split the project into two, one for the screen, and then the full ad as you have it to fit on an A6 post card. So here are some update: Phone number should be written as (07482) 315907 Change spelling of Program to Programme (£600 Value) change to (Value £600) (£25) Value change to (Value £25) (£45 Value) change to (Value £45) For the screen replace the woman with my picture Also I just got this width to height ratio of the screen is 16:9 The important things to call out on the screen "Early Bird Offer Custom Kick Start Program" "Who Wants To Lose 15 Pounds and Be Healthy in 2015" The Cost of £200 The Savings of £470 The Expiration Date Limited to Fist 10 Individuals Enroll Now The screen should also tell people to pick up a flyer in the Waiting Room Then the flyer, remember just A6 post card should have the full Ad Thank you for taking the time to design my ad

Use colors in my logo. Important for the screen: So I've decided it makes sense to split the project into two, one for the screen, and then the full ad as you have it to fit on an A6 post card. So here are some update: Phone number should be written as (07482) 315907 Change spelling of Program to Programme (£600 Value) change to (Value £600) (£25) Value change to (Value £25) (£45 Value) change to (Value £45) For the screen replace the woman with my picture Also I just got this width to height ratio of the screen is 16:9 The important things to call out on the screen "Early Bird Offer Custom Kick Start Program" "Who Wants To Lose 15 Pounds and Be Healthy in 2015" Cost of £200 Savings of £470 The Expiration Date Limited to First 10 Individuals Enroll Now The screen should also tell people to pick up a flyer in the Waiting Room Then the flyer, remember just A6 post card should have the full Ad Thank you for taking the time to design my ad

Women in the age group of 25 to 60, who want to get strong and fit, but are afraid of the weight room. So measure about strength must be subtle or just not there at all. This is not a call for bodybuilders

• Use colors in my logo. Important for the screen:

So I've decided it makes sense to split the project into two, one for the screen, and then the full ad as you have it to fit on an A6 post card.

So here are some update:

Phone number should be written as (07482) 315907
Change spelling of Program to Programme
(£600 Value) change to (Value £600)
(£25) Value change to (Value £25)
(£45 Value) change to (Value £45)
For the screen replace the woman with my picture

Also I just got this width to height ratio of the screen is 16:9

The important things to call out on the screen
"Early Bird Offer Custom Kick Start Program"
"Who Wants To Lose 15 Pounds and Be Healthy in 2015"
The Cost of £200
The Savings of £470
The Expiration Date
Limited to Fist 10 Individuals
Enroll Now

The screen should also tell people to pick up a flyer in the Waiting Room

Then the flyer, remember just A6 post card should have the full Ad

Thank you for taking the time to design my ad

```html
<!DOCTYPE html>
<html lang="en">
<head>
<meta charset="utf-8">
<title>TrueForm Habits – Early Bird Offer</title>
<link rel="stylesheet" href="https://fonts.googleapis.com/css2?family=Archivo+Black&family=Open+Sans:wght@300;400;600;700;800&display=swap">
<style>
  :root {
    --sky: #1fa0e3;
    --sky-light: #8fd0f3;
    --sky-deep: #1a86c9;
    --red: #d3202e;
    --grey: #7b7d80;
    --ink: #111111;
    --white: #ffffff;
    --coral-top: #f07a6a;
    --coral-bottom: #e9574f;
  }
  html, body {
    margin: 0;
    padding: 0;
    overflow: hidden;
    background: var(--white);
  }
  .screen-ad {
    position: relative;
    width: 1200px;
    height: 675px;
    overflow: hidden;
    background: var(--white);
    font-family: "Open Sans", Arial, sans-serif;
    color: var(--ink);
  }
  .backdrop {
    position: absolute;
    inset: 0;
  }
  .brand {
    position: absolute;
    left: 16px;
    top: 60px;
    display: flex;
    align-items: center;
    gap: 8px;
  }
  .brand-mark {
    width: 15px;
    height: 15px;
    background: var(--red);
  }
  .brand-name {
    font-weight: 800;
    font-size: 19px;
    color: var(--sky-deep);
    white-space: nowrap;
  }
  .offer-title {
    position: absolute;
    left: 212px;
    top: 60px;
    margin: 0;
    font-weight: 800;
    font-size: 18px;
    line-height: 30px;
    white-space: nowrap;
  }
  .offer-title .programme-name {
    font-size: 22px;
  }
  .trainer-photo {
    position: absolute;
    left: 205px;
    top: 120px;
    width: 320px;
    height: 510px;
    border-radius: 150px 150px 20px 20px;
    background: linear-gradient(180deg, #c99a80 0%, #b07a5e 40%, var(--coral-top) 48%, var(--coral-bottom) 100%);
  }
  .headline {
    position: absolute;
    left: 546px;
    top: 122px;
    margin: 0;
    font-weight: 300;
    white-space: nowrap;
  }
  .headline > .line { display: block; }
  .headline .line-ask,
  .headline .line-goal,
  .headline .line-health {
    font-size: 58px;
    line-height: 68px;
  }
  .headline .line-ask { color: var(--sky); }
  .headline .asterisk {
    color: var(--red);
    font-size: 36px;
    vertical-align: top;
    line-height: 36px;
  }
  .headline .line-goal { color: var(--red); }
  .headline .line-health { color: var(--grey); }
  .headline .line-year {
    font-size: 104px;
    line-height: 108px;
    color: var(--sky);
    letter-spacing: -2px;
  }
  .enrol {
    position: absolute;
    left: 548px;
    top: 440px;
    line-height: 1.25;
    font-size: 22px;
  }
  .enrol p { margin: 0; }
  .enrol .limit { color: var(--red); }
  .enrol .limit strong { font-weight: 400; font-size: 28px; line-height: 1; }
  .enrol .action { color: var(--grey); font-weight: 600; }
  .enrol .contact { color: var(--sky); }
  .enrol .phone {
    color: var(--red);
    font-size: 42px;
    margin-top: 2px;
    letter-spacing: 0.5px;
  }
  .price-tag {
    position: absolute;
    left: 28px;
    top: 462px;
    transform: rotate(-5deg);
    font-family: "Archivo Black", Arial, sans-serif;
    line-height: 1;
  }
  .price-tag .only {
    display: block;
    font-size: 44px;
    color: var(--sky);
    margin-left: 8px;
  }
  .price-tag .amount {
    display: block;
    font-size: 62px;
    color: var(--red);
  }
  .savings {
    position: absolute;
    left: 1014px;
    top: 24px;
    width: 220px;
    transform: rotate(50deg);
    text-align: center;
    font-weight: 800;
    line-height: 1;
    color: var(--ink);
  }
  .savings .save { display: block; font-size: 24px; }
  .savings .save-amount { display: block; font-size: 38px; }
  .savings .expiry-label { display: block; font-size: 18px; }
  .savings .expiry-date { display: block; font-size: 34px; }
  .flyer-note {
    position: absolute;
    left: 0;
    right: 0;
    bottom: 4px;
    margin: 0;
    text-align: center;
    color: var(--white);
    font-weight: 700;
    font-size: 23px;
  }
</style>
</head>
<body>
<main class="screen-ad">
  <svg class="backdrop" width="1200" height="675" viewBox="0 0 1200 675" aria-hidden="true">
    <defs>
      <linearGradient id="swoosh-right" x1="0" y1="0" x2="1" y2="0">
        <stop offset="0" stop-color="#c9e9fa"/>
        <stop offset="0.5" stop-color="#2aa7e6"/>
        <stop offset="1" stop-color="#1a86c9"/>
      </linearGradient>
      <pattern id="corner-stripes" width="26" height="26" patternUnits="userSpaceOnUse" patternTransform="rotate(45)">
        <rect width="26" height="26" fill="#9fd6f4"/>
        <rect width="10" height="26" fill="#1fa0e3"/>
      </pattern>
    </defs>
    <path d="M370 0 Q720 42 1090 0 Z" fill="var(--sky)"/>
    <path d="M1200 110 C1140 250 1130 420 1200 580 Z" fill="url(#swoosh-right)"/>
    <path d="M1200 200 C1165 300 1160 420 1200 520 Z" fill="#5bbdee"/>
    <path d="M0 628 C380 588 820 588 1200 598 L1200 616 C820 606 380 606 0 646 Z" fill="var(--sky-light)"/>
    <path d="M0 640 C380 604 820 602 1200 612 L1200 675 L0 675 Z" fill="var(--sky)"/>
    <path d="M965 0 L1200 0 L1200 240 Z" fill="url(#corner-stripes)"/>
    <path d="M965 0 C1040 45 1135 135 1200 240 C1145 170 1050 80 965 0 Z" fill="#ffffff" opacity="0.85"/>
  </svg>

  <div class="brand">
    <span class="brand-mark"></span>
    <span class="brand-name">TrueForm Habits</span>
  </div>

  <h1 class="offer-title">EARLY BIRD OFFER CUSTOM <span class="programme-name">FRESH RALLY QUEST PROGRAMME</span></h1>

  <div class="trainer-photo" role="img" aria-label="Photo of the personal trainer in a coral vest, smiling"></div>

  <h2 class="headline">
    <span class="line line-ask"><span class="asterisk">*</span>Who wants to</span>
    <span class="line line-goal">lose 15 pounds</span>
    <span class="line line-health">and be healthy</span>
    <span class="line line-year">in 2015?</span>
  </h2>

  <div class="enrol">
    <p class="limit">Limited to the first <strong>10</strong> individuals to</p>
    <p class="action">Enrol Now</p>
    <p class="contact">Call and ask for Dana</p>
    <p class="phone">(07482) 315907</p>
  </div>

  <div class="price-tag">
    <span class="only">ONLY</span>
    <span class="amount">£200</span>
  </div>

  <div class="savings">
    <span class="save">SAVE</span>
    <span class="save-amount">£470</span>
    <span class="expiry-label">Offer Expires</span>
    <span class="expiry-date">31/12/14</span>
  </div>

  <p class="flyer-note">For more details pick up card from table near entrance</p>
</main>
</body>
</html>
```